Storage Company Newsletter

We need a design for a newsletter for our company Vaultnest, a digital and physical asset storage company .The newsletter will be informative and educational covering tips on secure storage of personal documents and items both at home and at the work place. Rest easy with Vaultnest is our mantra. We have a pre-existing trademark & logo. Colors are blue and green. We can share the cmyk/rgb color information and background is grey.

Target Market(s)

Mass market – Middle to High income individuals

Industry/Entity Type

Digital

Font styles to use
Sans Serif

Colors
0393ce
00a88f
edf2f7

Requirements
Must have
• The newsletter linked to a CMS. In HTML5; Mail-chimp integration readable on Gmail, Yahoo, Hotmail and Outlook
Nice to have
• Sections of the newsletter are:
• Cover story
• News Flash
• Mwanachi Perspective
• Spotlight on the Counties
• CEO's Corner
• Tips and Helpful Information
• Important Dates and Events

```html
<!DOCTYPE html>
<html lang="en">
<head>
<meta charset="utf-8">
<title>Vaultnest Newsletter</title>
<link rel="stylesheet" href="https://fonts.googleapis.com/css2?family=Archivo:wght@400;600;800;900&family=Open+Sans:wght@400;600;700&display=swap">
<style>
:root{
  --blue:#0393ce;
  --blue-band:#3b8fd9;
  --green:#00a88f;
  --mist:#edf2f7;
  --page:#656b74;
  --ink:#222831;
  --text:#5b6370;
  --white:#ffffff;
  --teal-bar:#3fc3cf;
}
*{box-sizing:border-box;margin:0;padding:0}
html,body{width:1200px;height:3500px;overflow:hidden}
body{background:var(--page);font-family:"Open Sans",Arial,sans-serif;color:var(--text)}
.newsletter{position:absolute;left:200px;top:16px;width:800px}
h1,h2,h3,.btn,.nav a{font-family:"Archivo",Arial,sans-serif}

.topbar{height:54px;background:var(--teal-bar);display:flex;justify-content:center;align-items:center;gap:10px}
.topbar svg{display:block}

.hero{position:relative;height:334px;margin-top:14px;color:var(--white);text-align:center}
.hero-photo{position:absolute;inset:0;background:linear-gradient(180deg,#2f6fb8 0%,#5a9ee0 45%,#3f7fc6 100%)}
.hero-shade{position:absolute;inset:0;background:linear-gradient(180deg,rgba(10,40,90,.25),rgba(10,40,90,.1))}
.hero-head{position:relative;display:flex;justify-content:space-between;align-items:flex-start;padding:18px 30px 0}
.brand{display:flex;align-items:center;gap:8px;font-family:"Archivo",Arial,sans-serif;font-weight:800;font-size:20px;color:var(--white)}
.brand-mark{width:22px;height:22px;background:var(--green)}
.nav{display:flex;gap:34px;padding-top:4px}
.nav a{color:var(--white);text-decoration:none;font-size:11px;font-weight:600;letter-spacing:1px}
.hero-copy{position:relative;margin-top:92px}
.hero-copy h1{font-size:36px;font-weight:900;letter-spacing:.5px}
.hero-copy h1 span{color:var(--green)}
.hero-copy p{font-size:12px;max-width:300px;margin:10px auto 0;line-height:1.5;font-weight:600}
.btn{display:inline-block;font-size:10px;font-weight:800;letter-spacing:1px;padding:8px 18px;text-decoration:none}
.btn-ghost{border:1px solid var(--white);color:var(--white);margin-top:20px}
.btn-outline{border:2px solid var(--ink);color:var(--ink);background:var(--white)}
.btn-solid{background:var(--blue-band);color:var(--white);padding:9px 22px}

.intro{background:var(--white);padding:46px 60px 0}
.section-head{display:flex;justify-content:space-between;align-items:flex-start}
.section-head h2{font-size:34px;font-weight:900;color:var(--ink);line-height:1;letter-spacing:.3px;border-top:5px solid var(--ink);padding-top:12px}
.intro p{margin-top:24px;font-size:12.5px;line-height:1.65}
.intro-photos{display:grid;grid-template-columns:1fr 1fr;gap:6px;margin-top:26px;height:100px}
.photo{display:block}
.photo-stamp{background:linear-gradient(135deg,#b9b3a8,#6f6a62)}
.photo-seal{background:linear-gradient(135deg,#d8d2c2,#8a8476)}

.precaution{background:var(--blue-band);color:var(--white);text-align:center;padding:40px 90px 34px;margin-top:22px}
.precaution h2{font-size:19px;font-weight:600;line-height:1.35}
.precaution h3{font-size:13px;font-weight:600;margin-top:24px;letter-spacing:.5px}
.tips{background:var(--mist);padding:44px 60px 20px;display:grid;grid-template-columns:1fr 1fr;column-gap:70px;row-gap:36px;border-left:10px solid var(--blue-band);border-right:10px solid var(--blue-band);border-bottom:12px solid var(--blue-band)}
.tip h4{font-family:"Archivo",Arial,sans-serif;color:var(--green);font-size:14px;font-weight:800}
.tip p{font-size:12px;line-height:1.65;margin-top:14px}

.clients{background:var(--blue-band);color:var(--white);text-align:center;padding:30px 40px 34px}
.clients h2{font-size:19px;font-weight:600}
.client-row{display:flex;justify-content:space-around;align-items:center;margin-top:30px}
.client{display:flex;align-items:center;gap:8px;font-size:13px;font-weight:600}
.client i{width:16px;height:16px;border-radius:50%;background:var(--white)}

.cover{background:var(--white);padding:40px 60px 40px;margin-top:16px}
.cover>p{margin-top:24px;font-size:12.5px;line-height:1.65}
.story-grid{display:grid;grid-template-columns:1fr 1fr;gap:24px;margin-top:26px}
.story-photo{height:128px}
.photo-files{background:linear-gradient(135deg,#a48a63,#5b4c37)}
.photo-box{background:linear-gradient(135deg,#3d7c70,#1f4d46)}
.story h3{color:var(--blue-band);font-size:15px;font-weight:700;margin-top:14px}
.meta{font-size:10px;margin-top:6px;color:#7a818c}
.story p{font-size:12px;line-height:1.6;margin-top:10px}
.more{display:block;font-size:11px;color:var(--blue-band);font-weight:700;margin-top:8px;text-decoration:none}

.news-head{background:var(--blue-band);color:var(--white);text-align:center;height:62px;line-height:62px;margin-top:16px}
.news-head h2{font-size:19px;font-weight:600}
.news{background:var(--white);padding:28px 40px 36px;display:grid;grid-template-columns:repeat(3,1fr);gap:20px}
.news-photo{height:136px;background:linear-gradient(135deg,#e7ebef,#7b8fa5)}
.news-item h3{color:var(--blue-band);font-size:15px;font-weight:700;margin-top:14px}
.news-item p{font-size:12px;line-height:1.6;margin:10px 0 16px}
</style>
</head>
<body>
<div class="newsletter">
  <div class="topbar">
    <svg width="10" height="10" viewBox="0 0 10 10"><circle cx="5" cy="5" r="4" fill="none" stroke="#fff" stroke-width="1.5"/></svg>
    <svg width="10" height="10" viewBox="0 0 10 10"><rect x="1" y="1" width="8" height="8" fill="none" stroke="#fff" stroke-width="1.5"/></svg>
    <svg width="10" height="10" viewBox="0 0 10 10"><circle cx="5" cy="5" r="4" fill="none" stroke="#fff" stroke-width="1.5"/></svg>
  </div>

  <header class="hero">
    <div class="hero-photo" role="img" aria-label="Photo of rows of blue metal safe deposit lockers"></div>
    <div class="hero-shade"></div>
    <div class="hero-head">
      <div class="brand"><i class="brand-mark"></i>Vaultnest</div>
      <nav class="nav"><a href="#">HOME</a><a href="#">BLOG</a><a href="#">PORTFOLIO</a><a href="#">CONTACT</a></nav>
    </div>
    <div class="hero-copy">
      <h1>REST EASY WITH <span>VAULTNEST</span></h1>
      <p>Secure storage of personal documents and items both at home and at the work place</p>
      <a class="btn btn-ghost" href="#">FIND OUT MORE</a>
    </div>
  </header>

  <section class="intro">
    <div class="section-head">
      <h2>CARING<br>FOR VALUABLE<br>DOCUMENTS</h2>
      <a class="btn btn-outline" href="#">MORE ABOUT US</a>
    </div>
    <p>Valuable documents include a wide range of items such as land title deeds, certificates, letters, photographs, newspaper cuttings and memorabilia. The longevity of these items can be threatened by numerous factors such as light, moisture, insects such as silverfish, and physical damage. By taking these simple precautions outlined below, you can preserve your valuable documents and keep them for posterity.</p>
    <div class="intro-photos">
      <div class="photo photo-stamp" role="img" aria-label="Photo of an embossing seal stamp on paper"></div>
      <div class="photo photo-seal" role="img" aria-label="Photo of an official embossed document seal"></div>
    </div>
  </section>

  <section class="precaution">
    <h2>SIMPLE PRECAUTION TO PRESERVE YOUR VALUABLE DOCUMENTS AND KEEP THEM FOR POSTERITY</h2>
    <h3>TIPS AND HELPFUL INFORMATION</h3>
  </section>
  <div class="tips">
    <div class="tip"><h4># 1</h4><p>Valuable documents should be stored off the floor and away from external walls or windows, to protect them from dramatic fluctuations in temperature and humidity. Storage areas must remain dry to prevent mould growth and water damage.</p></div>
    <div class="tip"><h4># 2</h4><p>To avoid unnecessary wear and tear on original documents, make several copies for reference and circulation. Avoid continual copying of original documents. When photocopying, use an extra copy to make copies from in the future.</p></div>
    <div class="tip"><h4># 3</h4><p>Ensure that equipment such as scanners and photocopiers are clean before placing your documents on them. Alternatively, copying them inside a plastic sleeve will keep the documents clean and help to support fragile documents during copying.</p></div>
    <div class="tip"><h4># 4</h4><p>Valuable documents should be stored in protective plastic sleeves. Use archival folders or enclosures as folding weakens the paper and rolling can make it difficult to view the item without damaging it.</p></div>
    <div class="tip"><h4># 5</h4><p>Do not laminate your valuable documents. The trust irreversible process that permanently embeds the document in plastic and adhesive. Documents treated in this manner will become permanently disfigured.</p></div>
    <div class="tip"><h4># 6</h4><p>Never use metal paperclips, staples and pins. These can rust and cause irreversible staining to paper items. Glasses are available that contain pockets of varying sizes so that diverse materials can be placed together in a folder or a sleeve.</p></div>
  </div>

  <section class="clients">
    <h2>OUR CLIENTS</h2>
    <div class="client-row">
      <span class="client"><i></i>Harborline</span>
      <span class="client"><i></i>Kestrel Media</span>
      <span class="client"><i></i>Orbit Global</span>
      <span class="client"><i></i>Northwind Life</span>
    </div>
  </section>

  <section class="cover">
    <div class="section-head">
      <h2>COVER<br>STORY</h2>
      <a class="btn btn-outline" href="#">READ MORE</a>
    </div>
    <p>Keep your most valued papers safe with care you can trust. Our experts share storage advice for the home, the office and everywhere in between, so your documents stay whole and easy to find.</p>
    <div class="story-grid">
      <article class="story">
        <div class="story-photo photo-files" role="img" aria-label="Photo of an expanding paper file folder"></div>
        <h3>Secure Documents &amp; Assets Storage</h3>
        <div class="meta">Written by Vaultnest / February 3 2016</div>
        <p>Sort papers by type and date, keep them in labelled archival boxes and store them in a cool, dry and locked place.</p>
        <a class="more" href="#">Read more</a>
      </article>
      <article class="story">
        <div class="story-photo photo-box" role="img" aria-label="Photo of a green archive storage box"></div>
        <h3>Secure Documents &amp; Assets Storage</h3>
        <div class="meta">Written by Vaultnest / February 3 2016</div>
        <p>Choose acid free boxes with close fitting lids, lift them with both hands and never stack them too high on a shelf.</p>
        <a class="more" href="#">Read more</a>
      </article>
    </div>
  </section>

  <div class="news-head"><h2>NEWS FLASH</h2></div>
  <section class="news">
    <article class="news-item">
      <div class="news-photo" role="img" aria-label="Photo of a hand signing a document"></div>
      <h3>News Flash # 1</h3>
      <p>New vault units open this month, with longer hours and simple online booking for every member.</p>
      <a class="btn btn-solid" href="#">Read more</a>
    </article>
    <article class="news-item">
      <div class="news-photo" role="img" aria-label="Photo of a hand signing a document"></div>
      <h3>News Flash # 2</h3>
      <p>Our digital archive now scans and backs up your papers, keeping a safe copy always in reach.</p>
      <a class="btn btn-solid" href="#">Read more</a>
    </article>
    <article class="news-item">
      <div class="news-photo" role="img" aria-label="Photo of a hand signing a document"></div>
      <h3>News Flash # 3</h3>
      <p>Join our free workshop on home storage and learn how to protect family records for years.</p>
      <a class="btn btn-solid" href="#">Read more</a>
    </article>
  </section>
</div>
</body>
</html>
```